TK Drafting

Simple Design - Logo is done (from this site). Logo on one side - Back Side an image or outline of a house blue print - My name, phone, email, website url. Prefer the traditional Architectural style of letters -

Target Market(s)

Customers who need a floor plan redesigned for renovations or realtors who want a floor plan for marketing their listings

Industry/Entity Type

Architecture

Contact Information for Business Card

Colin Varga - Name
318-542-6604 - Phone
tkdraftingco@mailvane.com
www.tkdraftingco.net

Font styles to use
Other font styles liked:
• Architecture writing -

Colors
0555a3
3276b5
85acd3

Requirements
Must have
• Logo that is attached. I like an indigo blue color for the background or a royal blue - gray logo OR - white and clean with the logo on one side and the same color gray lettering on the other side
Nice to have
• some sort of image that shows a residential blue print. It may not be possible on this small of a card though.
Should not have
• Nothing cartoonish.

```html
<!DOCTYPE html>
<html lang="en">
<head>
<meta charset="utf-8">
<title>TK Drafting – Business Card</title>
<link href="https://fonts.googleapis.com/css2?family=Roboto:wght@400;700&display=swap" rel="stylesheet">
<style>
  :root {
    --stage: #3a3a3c;
    --navy: #0d2e6b;
    --navy-deep: #0a2558;
    --mark-grey: #a9b8d8;
    --paper: #ffffff;
    --ink: #4a4a4a;
    --name-ink: #0d2e6b;
  }
  * { box-sizing: border-box; margin: 0; padding: 0; }
  html, body {
    width: 1200px; height: 900px; overflow: hidden;
    background: var(--stage);
    font-family: "Roboto", Arial, sans-serif;
  }
  .stage { position: relative; width: 1200px; height: 900px; }

  .card { position: absolute; box-shadow: 0 18px 40px rgba(0,0,0,.45); overflow: hidden; }

  /* Back: vertical, blue head + white contact panel */
  .card-back {
    left: 150px; top: 170px; width: 330px; height: 560px;
    background: var(--paper);
  }
  .card-back .head {
    height: 225px; background: var(--navy);
    display: flex; align-items: center; justify-content: center; gap: 12px;
  }
  .brand {
    color: var(--mark-grey); font-weight: 700; letter-spacing: .04em;
    text-transform: uppercase; white-space: nowrap;
  }
  .card-back .brand { font-size: 30px; }
  .brand-square { width: 18px; height: 18px; background: var(--mark-grey); flex: none; }

  .contact { padding: 34px 30px 0 34px; }
  .person-name { color: var(--name-ink); font-weight: 700; font-size: 24px; letter-spacing: .01em; text-transform: uppercase; }
  .person-role { color: var(--ink); font-size: 17px; margin-top: 2px; margin-bottom: 22px; }
  .line { display: flex; align-items: center; gap: 12px; color: var(--ink); font-size: 17px; margin-bottom: 10px; white-space: nowrap; }
  .line svg { width: 18px; height: 18px; flex: none; }

  /* Front: horizontal, full blue */
  .card-front {
    left: 560px; top: 250px; width: 520px; height: 330px;
    background: linear-gradient(160deg, var(--navy) 0%, var(--navy-deep) 100%);
    display: flex; align-items: center; justify-content: center; gap: 16px;
  }
  .card-front .brand { font-size: 44px; }
  .card-front .brand-square { width: 26px; height: 26px; }
</style>
</head>
<body>
<div class="stage">

  <section class="card card-back" aria-label="Business card back">
    <div class="head">
      <span class="brand-square"></span>
      <span class="brand">TK Drafting</span>
    </div>
    <div class="contact">
      <p class="person-name">Colin Varga</p>
      <p class="person-role">Director</p>
      <p class="line">
        <svg viewBox="0 0 24 24" aria-hidden="true"><path fill="#0d2e6b" d="M6.6 10.8a15.1 15.1 0 0 0 6.6 6.6l2.2-2.2a1 1 0 0 1 1-.25 11.4 11.4 0 0 0 3.6.57 1 1 0 0 1 1 1V20a1 1 0 0 1-1 1A17 17 0 0 1 3 4a1 1 0 0 1 1-1h3.5a1 1 0 0 1 1 1c0 1.25.2 2.45.57 3.57a1 1 0 0 1-.25 1z"/></svg>
        318-542-6604
      </p>
      <p class="line">
        <svg viewBox="0 0 24 24" aria-hidden="true"><rect x="2" y="4" width="20" height="16" rx="1" fill="#0d2e6b"/><path d="M3 6l9 7 9-7" fill="none" stroke="#fff" stroke-width="1.6"/></svg>
        tkdraftingco@mailvane.com
      </p>
      <p class="line">
        <svg viewBox="0 0 24 24" aria-hidden="true"><g fill="none" stroke="#0d2e6b" stroke-width="1.8"><circle cx="12" cy="12" r="9.5"/><ellipse cx="12" cy="12" rx="4" ry="9.5"/><path d="M2.5 12h19M4 7h16M4 17h16"/></g></svg>
        www.tkdraftingco.net
      </p>
    </div>
  </section>

  <section class="card card-front" aria-label="Business card front">
    <span class="brand-square"></span>
    <span class="brand">TK Drafting</span>
  </section>

</div>
</body>
</html>
```